New CI for Powerpoint Catalogue & Stationary

We are selling premium promotional gifts made of
- nuts, chocolate, -> mainly for christmans
- icecreampowder and BBQ Rubs -> mainly for summer.

We need a new design for our powerpoint catalogue & stationary.

In order to highlight our sustainabilty approach, we deceided to go for the colors green, brown & white. I am happy with that choice but I want a new look.

We are building a new website under brovekind.de/cms.

The final design should communicate sustainabilty, premium quality and delicious products.

Target Market(s)

Companies looking for a premium gift for the clients or employees

Font styles to use
Other font styles liked:
• Memphis

```html
<!DOCTYPE html>
<html lang="de">
<head>
<meta charset="utf-8">
<title>Brovekind – Geschäftsausstattung</title>
<link href="https://fonts.googleapis.com/css2?family=Arvo:wght@400;700&display=swap" rel="stylesheet">
<style>
  :root {
    --green: #62bb46;
    --brown: #6e3a2e;
    --footer: #6b3a30;
    --kraft: #b8946a;
    --kraft-light: #c4a47a;
    --paper: #ffffff;
    --backdrop: #d6d6d6;
    --window: #cfcfcf;
    --rule: #d9d2cf;
  }
  * { box-sizing: border-box; margin: 0; padding: 0; }
  html, body { width: 733px; height: 1200px; overflow: hidden; }
  body {
    background: var(--backdrop);
    font-family: "Arvo", serif;
    color: var(--brown);
    position: relative;
  }
  .sheet { position: absolute; overflow: hidden; }

  /* Brand lockup: name in text font with a plain white circle plate */
  .brand-plate {
    position: absolute;
    border-radius: 50%;
    background: var(--paper);
    display: flex; align-items: center; justify-content: center;
  }
  .brand-name { font-family: "Arvo", serif; font-weight: 400; color: var(--brown); letter-spacing: .04em; }

  .band { position: absolute; top: 0; bottom: 0; background: var(--green); }

  /* Envelope front */
  .envelope-front { left: 17px; top: 26px; width: 344px; height: 172px; background: var(--paper); }
  .envelope-front .window {
    position: absolute; left: 31px; top: 79px; width: 139px; height: 72px;
    background: var(--window); border: 1px solid #b5b5b5; border-radius: 5px;
    display: flex; align-items: center; justify-content: center;
    font-size: 14px; color: #a88c80; letter-spacing: .02em;
  }
  .envelope-front .band { left: 222px; width: 70px; }
  .envelope-front .brand-plate { left: 215px; top: 45px; width: 84px; height: 84px; border: 2px solid var(--green); }
  .envelope-front .brand-name { font-size: 12px; }

  /* Envelope back */
  .envelope-back { left: 371px; top: 26px; width: 344px; height: 172px; background: var(--kraft); }
  .envelope-back .flap {
    position: absolute; left: 10px; top: 0; width: 324px; height: 59px;
    background: var(--paper); border-radius: 0 0 14px 14px;
  }
  .envelope-back .band { left: 51px; width: 70px; top: 59px; }
  .envelope-back .seal { left: 50px; top: 97px; width: 72px; height: 72px; }
  .envelope-back .brand-name { font-size: 10px; }

  /* Letterhead */
  .letterhead { left: 17px; top: 220px; width: 300px; height: 424px; background: var(--paper); }
  .letterhead .band { left: 118px; width: 64px; bottom: auto; height: 95px; }
  .letterhead .brand-plate { left: 111px; top: 20px; width: 78px; height: 78px; }
  .letterhead .brand-name { font-size: 12px; }
  .slogan { position: absolute; left: 0; right: 0; text-align: center; font-size: 6px; color: var(--brown); }
  .letterhead .slogan { top: 373px; }

  .footer-bar {
    position: absolute; left: 0; right: 0; bottom: 0; background: var(--footer);
    color: #e8d6c8; font-size: 5.2px; line-height: 1.6;
    display: flex; justify-content: space-between; align-items: center;
  }
  .letterhead .footer-bar { height: 32px; padding: 0 20px; }
  .footer-contacts { display: grid; grid-template-columns: auto auto; column-gap: 9px; }
  .footer-contacts span { display: flex; align-items: center; gap: 3px; }
  .footer-contacts svg { width: 5px; height: 5px; fill: var(--green); flex: none; }

  /* Kraft sheet */
  .kraft-sheet { left: 332px; top: 220px; width: 300px; height: 424px; background: linear-gradient(160deg, var(--kraft-light), var(--kraft)); }

  /* Order form */
  .order-form { left: 31px; top: 687px; width: 323px; height: 458px; background: var(--paper); }
  .order-form .band { left: 138px; width: 46px; bottom: auto; height: 76px; }
  .order-form .brand-plate { left: 132px; top: 14px; width: 58px; height: 58px; }
  .order-form .brand-name { font-size: 9px; }
  .order-title {
    position: absolute; left: 15px; right: 15px; top: 95px; display: flex; align-items: center; gap: 8px;
    font-size: 11px; font-weight: 700; color: var(--brown);
  }
  .order-title::before, .order-title::after { content: ""; flex: 1; height: 1px; background: var(--rule); }
  .order-note { position: absolute; left: 0; right: 0; top: 112px; text-align: center; font-size: 4.2px; font-weight: 700; line-height: 1.35; }
  .address-block { position: absolute; top: 140px; font-size: 4px; font-weight: 700; line-height: 1.35; }
  .address-block.to { left: 15px; }
  .address-block.ship { left: 165px; }
  .order-table { position: absolute; left: 15px; width: 293px; border-collapse: collapse; font-size: 4px; }
  .order-table th { background: var(--green); color: #fff; font-weight: 700; height: 8px; padding: 0 3px; text-align: left; border-right: 1px solid #fff; }
  .order-table td { height: 9px; padding: 0 3px; border-bottom: 1px dotted var(--rule); }
  .order-table.meta { top: 186px; }
  .order-table.meta th, .order-table.meta td { text-align: center; }
  .order-table.items { top: 215px; }
  .order-table .num { text-align: right; }
  .totals { position: absolute; right: 15px; top: 311px; font-size: 4px; font-weight: 700; }
  .totals div { display: flex; justify-content: flex-end; gap: 8px; height: 9.5px; align-items: center; border-bottom: 1px solid var(--rule); width: 110px; }
  .totals .value { width: 32px; text-align: right; }
  .totals .grand { border-top: 1px solid var(--brown); }
  .remarks { position: absolute; left: 15px; top: 368px; width: 175px; font-size: 4px; font-weight: 700; padding-top: 3px; border-top: 1px solid var(--rule); }
  .approval { position: absolute; left: 163px; top: 399px; width: 145px; font-size: 4px; font-weight: 700; padding-top: 3px; border-top: 1px solid var(--rule); display: flex; justify-content: space-between; }
  .order-form .slogan { top: 418px; }
  .order-form .footer-bar { height: 30px; padding: 0 22px; }

  /* Notebook */
  .notebook { left: 400px; top: 757px; width: 295px; height: 404px; background: linear-gradient(165deg, var(--kraft-light), var(--kraft)); border-radius: 4px; }
  .notebook .spine { position: absolute; left: 0; top: 0; bottom: 0; width: 59px; background: var(--green); }
  .notebook .rings { position: absolute; left: -10px; top: 10px; bottom: 10px; width: 18px; display: flex; flex-direction: column; justify-content: space-between; }
  .notebook .rings span { display: block; height: 5px; border: 1.5px solid #6b6b6b; border-radius: 3px; background: #eee; }
  .notebook .cover-brand { position: absolute; left: 59px; right: 0; top: 185px; text-align: center; }
  .notebook .cover-brand .brand-name { font-size: 22px; display: block; }
  .notebook .cover-brand .tagline { font-size: 7px; letter-spacing: .25em; color: var(--brown); display: block; margin-top: 6px; }
  .notebook .mark-dot { width: 22px; height: 22px; border-radius: 50%; background: var(--brown); margin: 0 auto 10px; }
</style>
</head>
<body>

<section class="sheet envelope-front" aria-label="Briefumschlag Vorderseite">
  <div class="window">WINDOW</div>
  <div class="band"></div>
  <div class="brand-plate"><span class="brand-name">brovekind</span></div>
</section>

<section class="sheet envelope-back" aria-label="Briefumschlag Rückseite">
  <div class="flap"></div>
  <div class="band"></div>
  <div class="brand-plate seal"><span class="brand-name">brovekind</span></div>
</section>

<section class="sheet letterhead" aria-label="Briefbogen">
  <div class="band"></div>
  <div class="brand-plate"><span class="brand-name">brovekind</span></div>
  <p class="slogan">&lt;Slogan geht hier&gt;</p>
  <footer class="footer-bar">
    <div>Brovekind Premium Snacks GmbH<br>Lindenstieg 14 22301 Hamburg</div>
    <div class="footer-contacts">
      <span><svg viewBox="0 0 10 10"><circle cx="5" cy="5" r="5"/></svg>+49 (0) 40 555 012-50</span>
      <span><svg viewBox="0 0 10 10"><rect x="0" y="2" width="10" height="6"/></svg>nachschub@brovekind.de</span>
      <span><svg viewBox="0 0 10 10"><rect x="1" y="1" width="8" height="8"/></svg>+49 (0) 40 555 012-52</span>
      <span><svg viewBox="0 0 10 10"><circle cx="5" cy="5" r="5"/></svg>www.brovekind.de</span>
    </div>
  </footer>
</section>

<section class="sheet kraft-sheet" aria-label="Kraftpapierbogen"></section>

<section class="sheet order-form" aria-label="Bestellformular">
  <div class="band"></div>
  <div class="brand-plate"><span class="brand-name">brovekind</span></div>
  <h1 class="order-title">BESTELLUNG</h1>
  <p class="order-note">Die folgende Nummer muss auf allen verwandten erscheinen<br>Korrespondenz, Versandpapiere und Rechnungen:<br>P.O. NUMMER: [100]</p>
  <div class="address-block to">ZU:<br>Kundenname<br>Physikalische Adresse<br>P.O. Box<br>T: (000) 000-000<br>F: (000) 000-000</div>
  <div class="address-block ship">Versand an: Bitte geben Sie so viele Informationen wie<br>möglich an. Karten sind sehr hilfreich.<br>[Name]<br>[Name der Firma]<br>[Adresse]<br>[Stadt, ST Postleitzahl]<br>[Telefon]</div>
  <table class="order-table meta">
    <tr><th>P.O. DATUM</th><th>ANFORDERER</th><th>VERSENDET ÜBER</th><th>VERSANDDATUM</th><th>BEDINGUNGEN</th></tr>
    <tr><td>20/5/2021</td><td>Deinen Namen hier</td><td>Werde anrufen</td><td>1/21/07</td><td>Netto 30</td></tr>
  </table>
  <table class="order-table items">
    <tr><th>MENGE</th><th>EINHEIT</th><th>BESCHREIBUNG</th><th class="num">STÜCKPREIS</th><th class="num">GESAMT</th></tr>
    <tr><td>1</td><td>Rustkosten</td><td>Ihr Motiv auf der Folie (ab 5.000 Stück)</td><td class="num">€99,95</td><td class="num">€99,95</td></tr>
    <tr><td>1</td><td>Druckkosten</td><td>Ihr Motiv auf der Folie (ab 5.000 Stück)</td><td class="num">€99,95</td><td class="num">€99,95</td></tr>
    <tr><td></td><td></td><td></td><td></td><td></td></tr>
    <tr><td></td><td></td><td></td><td></td><td></td></tr>
    <tr><td></td><td></td><td></td><td></td><td></td></tr>
    <tr><td></td><td></td><td></td><td></td><td></td></tr>
  </table>
  <div class="totals">
    <div><span>ZWISCHENSUMME</span><span class="value"></span></div>
    <div><span>MEHRWERTSTEUER</span><span class="value"></span></div>
    <div><span>VERSAND &amp; BEARBEITUNG</span><span class="value"></span></div>
    <div><span>ANDERE</span><span class="value"></span></div>
    <div class="grand"><span>GESAMT</span><span class="value">€199,90</span></div>
  </div>
  <p class="remarks">Hinweise an uns, die sich auf Ihren Kauf beziehen</p>
  <p class="approval"><span>Genehmigt von</span><span>Datum</span></p>
  <p class="slogan">&lt;Slogan geht hier&gt;</p>
  <footer class="footer-bar">
    <div>Brovekind Premium Snacks GmbH<br>Lindenstieg 14 22301 Hamburg</div>
    <div class="footer-contacts">
      <span><svg viewBox="0 0 10 10"><circle cx="5" cy="5" r="5"/></svg>+49 (0) 40 555 012-50</span>
      <span><svg viewBox="0 0 10 10"><rect x="0" y="2" width="10" height="6"/></svg>nachschub@brovekind.de</span>
      <span><svg viewBox="0 0 10 10"><rect x="1" y="1" width="8" height="8"/></svg>+49 (0) 40 555 012-52</span>
      <span><svg viewBox="0 0 10 10"><circle cx="5" cy="5" r="5"/></svg>www.brovekind.de</span>
    </div>
  </footer>
</section>

<section class="sheet notebook" aria-label="Notizbuch">
  <div class="spine"></div>
  <div class="rings">
    <span></span><span></span><span></span><span></span><span></span><span></span><span></span><span></span><span></span><span></span><span></span><span></span><span></span><span></span><span></span><span></span><span></span><span></span><span></span><span></span>
  </div>
  <div class="cover-brand">
    <div class="mark-dot"></div>
    <span class="brand-name">brovekind</span>
    <span class="tagline">PREMIUM SNACKS</span>
  </div>
</section>

</body>
</html>
```